Whole Body Cryotherapy Business needs a Brochure

We need a brochure for marketing events of our spa. The name of the business is FrostVale. Our website is www.glacierhaven.example. We are located in New York City at the Marlowe Arcade. We need an eye catching brochure that discusses the health benefits of whole body cryotherapy. We need an editable file to be able to tweak the language of the brochure. The contact information that should be on the brochure is as follows:

FrostVale
Marlowe Arcade, 482 W. 31st Avenue
New York, NY 10047

Phone: (855) 614-3098

EMail: glacierhaven@mailbox.example

We prefer a color scheme that mainly uses blue, but are open to any design that is eye catching.

We need the brochure to fit on 8.5" x 11" paper.

Requirements
Must have
• Must have space for the following paragraphs (use Lorem Ipsem and we can fill in later): (1) What is Whole Body Cryotherapy and (2) What makes FrostVale different.

```html
<!DOCTYPE html>
<html lang="en">
<head>
<meta charset="utf-8">
<title>FrostVale – Whole Body Cryotherapy Brochure</title>
<link rel="stylesheet" href="https://fonts.googleapis.com/css2?family=Questrial&family=Montserrat:wght@400;600&display=swap">
<style>
  :root {
    --paper: #ffffff;
    --mist-light: #eefcf5;
    --mist-mid: #c9f3df;
    --mist-deep: #9fe6c6;
    --accent-green: #3ded7a;
    --title-grey: #a4ada9;
    --frame-white: #ffffff;
    --ink: #0d1a12;
    --rule: #1a1a1a;
  }
  html, body {
    margin: 0;
    padding: 0;
    width: 927px;
    height: 1200px;
    overflow: hidden;
    background: var(--paper);
  }
  .brochure {
    position: relative;
    width: 927px;
    height: 1200px;
    overflow: hidden;
    font-family: "Montserrat", sans-serif;
    color: var(--ink);
  }
  .mist-backdrop {
    position: absolute;
    inset: 0;
    background:
      radial-gradient(ellipse 520px 360px at 120px 330px, var(--mist-deep), transparent 70%),
      radial-gradient(ellipse 600px 300px at 780px 720px, var(--mist-mid), transparent 70%),
      radial-gradient(ellipse 420px 260px at 300px 60px, var(--mist-mid), transparent 70%),
      radial-gradient(ellipse 500px 260px at 820px 1150px, var(--mist-mid), transparent 70%),
      linear-gradient(180deg, var(--mist-light), var(--paper) 55%, var(--mist-light));
  }
  .brand-title {
    position: absolute;
    left: 22px;
    top: 40px;
    margin: 0;
    font-family: "Questrial", sans-serif;
    font-weight: 400;
    font-size: 128px;
    line-height: 118px;
    letter-spacing: -2px;
    color: var(--title-grey);
  }
  .brand-title .line-one { display: block; padding-left: 51px; }
  .brand-title .line-two { display: block; }
  .decor-lines {
    position: absolute;
    inset: 0;
    pointer-events: none;
  }
  .section-label {
    position: absolute;
    margin: 0;
    background: var(--accent-green);
    color: #fff;
    font-family: "Questrial", sans-serif;
    font-weight: 400;
    font-size: 19px;
    line-height: 24px;
    letter-spacing: 1.5px;
    text-transform: uppercase;
    box-sizing: border-box;
  }
  .label-what {
    left: 580px; top: 206px; width: 277px; height: 73px;
    padding: 16px 20px 0 10px;
    text-align: right;
  }
  .label-different {
    left: 55px; top: 591px; width: 284px; height: 71px;
    padding: 13px 10px 0 18px;
    text-align: left;
  }
  .section-copy {
    position: absolute;
    margin: 0;
    font-weight: 600;
    font-size: 14.6px;
    line-height: 20.5px;
    letter-spacing: 0.4px;
  }
  .copy-what {
    right: 89px; top: 383px; width: 310px;
    text-align: right;
  }
  .copy-different {
    left: 73px; top: 765px; width: 310px;
    text-align: left;
  }
  .contact-footer {
    position: absolute;
    left: 55px;
    top: 1089px;
    width: 802px;
    border-top: 1.5px solid var(--rule);
  }
  .footer-address {
    position: absolute;
    left: 0;
    top: 16px;
    margin: 0;
    font-family: "Montserrat", sans-serif;
    font-style: normal;
    font-size: 12px;
    line-height: 13.5px;
    letter-spacing: -0.2px;
  }
  .footer-phone, .footer-email {
    position: absolute;
    top: 38px;
    margin: 0;
    font-family: "Questrial", sans-serif;
    font-size: 15px;
    letter-spacing: 0.5px;
  }
  .footer-phone { left: 275px; }
  .footer-email { right: -23px; }
</style>
</head>
<body>
<main class="brochure">
  <div class="mist-backdrop" role="img" aria-label="Soft mint-green watercolour smoke texture across the page"></div>

  <h1 class="brand-title"><span class="line-one">Frost</span><span class="line-two">-Vale</span></h1>

  <svg class="decor-lines" width="927" height="1200" viewBox="0 0 927 1200" aria-hidden="true">
    <g fill="none" stroke="var(--frame-white)" stroke-width="3">
      <rect x="465" y="282" width="392" height="357"/>
      <rect x="55" y="662" width="390" height="364"/>
      <polygon points="424,523 594,679 374,742"/>
    </g>
  </svg>

  <h2 class="section-label label-what">What is whole body cryotherapy</h2>
  <p class="section-copy copy-what">Lorem ipsum dolor sit amet, consectetur adipisicing elit, sed do eiusmod tempor incididunt ut labore et dolore magna aliqua. Ut enim ad minim veniam, quis nostrud exercitation ullamco</p>

  <h2 class="section-label label-different">What makes FrostVale different</h2>
  <p class="section-copy copy-different">Lorem ipsum dolor sit amet, consectetur adipisicing elit, sed do eiusmod tempor incididunt ut labore et dolore magna aliqua. Ut enim ad minim veniam, quis nostrud exercitation ullamco</p>

  <footer class="contact-footer">
    <address class="footer-address">FrostVale<br>Marlowe Arcade, 482 W. 31st Avenue<br>New York, NY 10047</address>
    <p class="footer-phone">Phone: (855) 614-3098</p>
    <p class="footer-email">EMail: glacierhaven@mailbox.example</p>
  </footer>
</main>
</body>
</html>
```